Recipe Card Design

I have a small kitchen store in Livingston Montana, and I would like to have recipe cards (4x6 postcard) designed with my logo, lines for recipe writing, all in black and white. My website is here: www.copperladlehouse.com

Store

```html
<!DOCTYPE html>
<html lang="en">
<head>
<meta charset="utf-8">
<title>Copper Ladle House – Recipe Card</title>
<link rel="stylesheet" href="https://fonts.googleapis.com/css2?family=Oswald:wght@200&family=Open+Sans:wght@300;400&family=Crimson+Text:ital@1&display=swap">
<style>
  :root {
    --ink: #1a1a1a;
    --frame: #231f20;
    --paper: #ffffff;
    --rule: #a8a8a8;
    --label: #444444;
    --muted: #555555;
    --utensil-top: #f4f4f4;
    --utensil-bottom: #e6e6e6;
    --edge: #d4d4d4;
    --stamp: #8a8a8a;
    --backdrop: #ececec;
  }
  * { box-sizing: border-box; margin: 0; padding: 0; }
  html, body { width: 1200px; height: 995px; overflow: hidden; background: var(--backdrop); }
  body { position: relative; font-family: "Open Sans", sans-serif; color: var(--ink); }

  .card { position: absolute; background: var(--paper); }
  .abs { position: absolute; }

  /* Front */
  .card-front { left: 290px; top: 25px; width: 620px; height: 480px; background: var(--frame); }
  .card-front .face { position: absolute; left: 15px; top: 15px; right: 15px; bottom: 15px; background: var(--paper); border-radius: 8px; }

  .brand-block { display: flex; flex-direction: column; align-items: center; justify-content: center; gap: 10px; width: 123px; height: 150px; }
  .brand-mark { width: 26px; height: 26px; background: var(--ink); }
  .brand-name { font-family: "Open Sans", sans-serif; font-weight: 400; font-size: 17px; line-height: 1.15; text-align: center; color: var(--ink); text-transform: uppercase; letter-spacing: 1px; }

  .recipe-title { font-family: "Oswald", sans-serif; font-weight: 200; font-size: 60px; line-height: 1; letter-spacing: 1px; }
  .field-label { font-size: 12px; font-weight: 300; color: var(--label); }
  .field-label--large { font-size: 14px; }
  .field-line { height: 1px; background: var(--rule); }
  .column-label { font-size: 11.5px; font-weight: 300; color: var(--label); text-transform: uppercase; }
  .ruled { display: flex; flex-direction: column; gap: 19.5px; }
  .ruled span { display: block; height: 1px; background: var(--rule); }
  .utensils { background: linear-gradient(180deg, var(--utensil-top), var(--utensil-bottom)); border-radius: 4px; }

  /* Back */
  .card-back { left: 270px; top: 530px; width: 660px; height: 440px; box-shadow: 0 0 0 1px var(--edge); }
  .card-back .brand-block { width: 120px; height: 130px; }
  .card-back .brand-name { font-size: 15px; }
  .tagline { font-family: "Crimson Text", serif; font-style: italic; font-size: 18px; line-height: 1.2; color: var(--muted); }
  .website { font-size: 13px; color: var(--label); }
  .divider { width: 1px; background: var(--rule); }
  .stamp-box { border: 1px solid var(--stamp); }
</style>
</head>
<body>

<section class="card card-front" aria-label="Recipe card front">
  <div class="face">
    <div class="abs brand-block" style="left:12px;top:14px;">
      <span class="brand-mark"></span>
      <span class="brand-name">Copper<br>Ladle<br>House</span>
    </div>

    <h1 class="abs recipe-title" style="left:154px;top:26px;">RECIPE</h1>

    <span class="abs field-label field-label--large" style="left:154px;top:94px;">for:</span>
    <span class="abs field-line" style="left:188px;top:110px;width:256px;"></span>

    <span class="abs field-label" style="left:154px;top:120px;">servings:</span>
    <span class="abs field-line" style="left:206px;top:134px;width:75px;"></span>
    <span class="abs field-label" style="left:309px;top:120px;">prep time:</span>
    <span class="abs field-line" style="left:372px;top:134px;width:72px;"></span>

    <div class="abs utensils" role="img" aria-label="Line drawing of a whisk, a ladle and a slotted spatula" style="left:470px;top:32px;width:98px;height:110px;"></div>

    <span class="abs column-label" style="left:17px;top:179px;">Ingredients:</span>
    <div class="abs ruled" style="left:17px;top:194px;width:157px;">
      <span></span><span></span><span></span><span></span><span></span><span></span>
      <span></span><span></span><span></span><span></span><span></span><span></span>
    </div>

    <span class="abs column-label" style="left:197px;top:179px;">Directions:</span>
    <div class="abs ruled" style="left:197px;top:194px;width:371px;">
      <span></span><span></span><span></span><span></span><span></span><span></span>
      <span></span><span></span><span></span><span></span><span></span><span></span>
    </div>
  </div>
</section>

<section class="card card-back" aria-label="Recipe card back">
  <div class="abs brand-block" style="left:28px;top:28px;">
    <span class="brand-mark"></span>
    <span class="brand-name">Copper<br>Ladle<br>House</span>
  </div>
  <p class="abs tagline" style="left:170px;top:48px;">A friendly kitchen shop<br>for every home cook</p>
  <p class="abs website" style="left:170px;top:118px;">www.copperladlehouse.com</p>

  <span class="abs divider" style="left:360px;top:150px;height:250px;"></span>

  <div class="abs stamp-box" style="right:30px;top:30px;width:110px;height:82px;"></div>

  <span class="abs field-line" style="left:385px;top:205px;width:245px;"></span>
  <span class="abs field-line" style="left:385px;top:255px;width:245px;"></span>
  <span class="abs field-line" style="left:385px;top:305px;width:245px;"></span>
  <span class="abs field-line" style="left:385px;top:355px;width:245px;"></span>
</section>

</body>
</html>
```